International Sustainable Cities NGO needs PPT Design

We need a PPT design for a presentation upcoming at a leading university on the East coast. The design needs to be clean and simple, professional and room for photos and maps. It's a presentation about citizen mapping and data collection for city planning/decision making.

Industry/Entity Type

University

```html
<!DOCTYPE html>
<html lang="en">
<head>
<meta charset="utf-8">
<title>Greenway Cities – Slide Templates</title>
<link href="https://fonts.googleapis.com/css2?family=Lato:wght@300;400;700;900&display=swap" rel="stylesheet">
<style>
:root{
  --backdrop:#57c5a0;
  --forest:#2d5645;
  --title:#2a5744;
  --ink:#3a4a44;
  --white:#ffffff;
  --link:#1a3fbf;
}
*{box-sizing:border-box;margin:0;padding:0}
html,body{width:1200px;height:1138px;overflow:hidden;background:var(--backdrop);font-family:'Lato',sans-serif}
.board{position:relative;width:1200px;height:1138px}
.slide{position:absolute;width:562px;height:316px;background:var(--white);overflow:hidden;box-shadow:0 2px 4px rgba(0,0,0,.18)}
.slide .frame{position:absolute;left:0;top:0;width:562px;height:316px}
.controls{position:absolute;left:4px;bottom:4px;display:flex;gap:4px}
.controls span{width:7px;height:7px;border-radius:50%;border:1px solid rgba(255,255,255,.45)}
.brand{position:absolute;right:10px;bottom:20px;color:var(--white);font-weight:300;text-align:center;line-height:1.1;white-space:nowrap}
.brand .l1{font-size:12px;letter-spacing:2.4px;display:block}
.brand .l2{font-size:8.5px;letter-spacing:3px;display:block}
.title{position:absolute;color:var(--title);font-weight:900;font-size:24px;line-height:28px;letter-spacing:.2px}
.body{position:absolute;color:var(--ink);font-size:7.6px;line-height:9.8px}
.photo{position:absolute}
.map{background:linear-gradient(135deg,#ecebdf 0%,#e3e6d4 40%,#dfe6e6 70%,#ece8da 100%)}
.city{background:linear-gradient(160deg,#b9d5ea 0%,#5d87ad 45%,#1f3b57 100%)}
.city2{background:linear-gradient(175deg,#bcd3e6 0%,#90aab9 50%,#2d3e40 100%)}
.flowers{background:linear-gradient(150deg,#2a2a2b 0%,#5b4550 50%,#221f21 100%)}
.lake{background:linear-gradient(180deg,#c9d2d6 0%,#8e9c9e 45%,#2f4644 70%,#6f8f93 100%)}
.right{text-align:right}
.justify{text-align:justify}
.partner{position:absolute;color:var(--title);font-size:30px;font-weight:400;letter-spacing:.5px}
.host{position:absolute;color:var(--title);font-weight:300;text-align:center;line-height:1.15}
.host .l1{font-size:22px;letter-spacing:4px;display:block}
.host .l2{font-size:15px;letter-spacing:5px;display:block}
.contact{position:absolute;left:14px;top:216px;font-size:6.6px;line-height:9.7px;color:#111}
.contact b{font-weight:700}
.contact a{color:var(--link)}
</style>
</head>
<body>
<main class="board">

  <section class="slide" style="left:30px;top:43px">
    <div class="photo map" style="left:25px;top:19px;width:396px;height:232px" role="img" aria-label="Street map of a city centre"></div>
    <h2 class="title" style="left:428px;top:23px">SINGLE<br>PHOTO<br>LARGE</h2>
    <p class="body" style="left:428px;top:108px;width:104px">Lorem ipsum dolor sit amet, consectetur adipiscing elit. Aliquam quis justo sit amet tellus scelerisque posuere. Etiam elit nunc, egestas a finibus ut, lacinia sagittis lacus. Suspendisse massa risus.</p>
    <svg class="frame" viewBox="0 0 562 316"><path d="M300 298 C420 290 500 285 562 190 L562 316 L300 316 Z" fill="var(--forest)"/><rect x="0" y="298" width="562" height="18" fill="var(--forest)"/></svg>
    <div class="brand"><span class="l1">GREENWAY</span><span class="l2">CITIES</span></div>
    <div class="controls"><span></span><span></span><span></span><span></span><span></span><span></span></div>
  </section>

  <section class="slide" style="left:609px;top:43px">
    <h2 class="title right" style="right:395px;top:67px">SINGLE<br>PHOTO<br>RIGHT</h2>
    <p class="body right" style="right:395px;top:152px;width:120px">Lorem ipsum dolor sit amet, consectetur adipiscing elit. Aliquam quis justo sit amet tellus scelerisque posuere. Etiam elit nunc, egestas a finibus ut, lacinia sagittis lacus. Suspendisse massa risus.</p>
    <div class="photo city" style="left:202px;top:64px;width:262px;height:169px" role="img" aria-label="Rendering of a futuristic glass skyline"></div>
    <svg class="frame" viewBox="0 0 562 316"><path d="M300 298 C420 290 500 285 562 190 L562 316 L300 316 Z" fill="var(--forest)"/><rect x="0" y="298" width="562" height="18" fill="var(--forest)"/></svg>
    <div class="brand"><span class="l1">GREENWAY</span><span class="l2">CITIES</span></div>
    <div class="controls"><span></span><span></span><span></span><span></span><span></span><span></span></div>
  </section>

  <section class="slide" style="left:30px;top:396px">
    <h2 class="title right" style="right:396px;top:52px">PHOTO<br>GALLERY</h2>
    <div class="photo city" style="left:178px;top:36px;width:116px;height:226px;clip-path:polygon(0 8%,100% 0,100% 92%,0 100%)" role="img" aria-label="Futuristic towers seen from below"></div>
    <div class="photo city2" style="left:302px;top:32px;width:116px;height:226px;clip-path:polygon(0 8%,100% 0,100% 92%,0 100%)" role="img" aria-label="Waterfront city with elevated transit"></div>
    <svg class="frame" viewBox="0 0 562 316"><path d="M300 298 C420 290 500 285 562 190 L562 316 L300 316 Z" fill="var(--forest)"/><rect x="0" y="298" width="562" height="18" fill="var(--forest)"/></svg>
    <div class="brand"><span class="l1">GREENWAY</span><span class="l2">CITIES</span></div>
    <div class="controls"><span></span><span></span><span></span><span></span><span></span><span></span></div>
  </section>

  <section class="slide" style="left:609px;top:396px">
    <div class="photo map" style="left:109px;top:30px;width:321px;height:140px" role="img" aria-label="Street map of a riverside city"></div>
    <h2 class="title" style="left:0;width:540px;top:182px;text-align:center">SINGLE PHOTO TOP</h2>
    <p class="body justify" style="left:196px;top:218px;width:147px">Lorem ipsum dolor sit amet, consectetur adipiscing elit. Aliquam quis justo sit amet tellus scelerisque posuere. Etiam elit nunc, egestas a finibus ut, lacinia sagittis lacus. Suspendisse massa risus.</p>
    <svg class="frame" viewBox="0 0 562 316"><path d="M300 298 C420 290 500 285 562 190 L562 316 L300 316 Z" fill="var(--forest)"/><rect x="0" y="298" width="562" height="18" fill="var(--forest)"/></svg>
    <div class="brand"><span class="l1">GREENWAY</span><span class="l2">CITIES</span></div>
    <div class="controls"><span></span><span></span><span></span><span></span><span></span><span></span></div>
  </section>

  <section class="slide" style="left:30px;top:754px">
    <div class="photo flowers" style="left:29px;top:29px;width:165px;height:258px" role="img" aria-label="Dark close-up of hydrangea flowers"></div>
    <div class="photo lake" style="left:198px;top:29px;width:166px;height:258px" role="img" aria-label="Mountain lake with reflections"></div>
    <h2 class="title" style="left:375px;top:50px">PHOTO<br>GALLERY<br>BIG LEFT</h2>
    <p class="body justify" style="left:375px;top:135px;width:121px">Lorem ipsum dolor sit amet, consectetur adipiscing elit. Aliquam quis justo sit amet tellus scelerisque posuere. Donec euismod metus ac sem varius, ac venenatis mauris varius. Vivamus non nisl eleifend, tristique tellus in, lobortis magna. Morbi in commodo purus.</p>
    <svg class="frame" viewBox="0 0 562 316"><path d="M300 298 C420 290 500 285 562 190 L562 316 L300 316 Z" fill="var(--forest)"/><rect x="0" y="298" width="562" height="18" fill="var(--forest)"/></svg>
    <div class="brand"><span class="l1">GREENWAY</span><span class="l2">CITIES</span></div>
    <div class="controls"><span></span><span></span><span></span><span></span><span></span><span></span></div>
  </section>

  <section class="slide" style="left:609px;top:754px">
    <h2 class="title" style="left:0;width:556px;top:70px;text-align:center">THANK YOU</h2>
    <div class="partner" style="left:98px;top:124px">civimap</div>
    <div class="host" style="left:346px;top:128px"><span class="l1">GREENWAY</span><span class="l2">CITIES</span></div>
    <div class="contact">
      <b>Dana Whitfield | Executive Director</b><br>
      <b>Greenway Cities | Greenway World Forum</b><br>
      120 Harbor Lane, Suite 40 | Riverton, CA 90000 | USA<br>
      t. 555.010.2040 | c. 555.010.3090 | <a>dana@greenwaycities.org</a><br>
      <a>www.greenwaycities.org</a><br>
      Public Profile<br>
      <a>https://www.example.com/in/dana-whitfield-a10482</a>
    </div>
    <svg class="frame" viewBox="0 0 562 316"><rect x="0" y="298" width="562" height="18" fill="var(--forest)"/></svg>
    <div class="controls"><span></span><span></span><span></span><span></span><span></span><span></span></div>
  </section>

</main>
</body>
</html>
```